The World Most Wanted Eyelahes

1. We need a web design for a new company based in California, USA
2. We are the manufacturer for 100% human hair eyelashes,
made in Indonesia.
3. We recently launched "Tapered Eyelashes" with human hair.
Currently, none of the people carried Tapered eyelash.
4. We would like to see designs that use the 4 different colors that match with my products as "Four Seasons" concepts.
5. We prefer to follow www.velkro.com style, like professional website.
6. Focus on products as a manufacturer, therefore, all wholesaler and retailer copy and paste to their marketing tools.
7. Need bilingual English and Spanish.
8. Easy to link with social media.

Target Market(s)

United States and Central/South America.

Industry/Entity Type

Hair

Number of Pages Required

5+ page

Requirements
Must have
• 1. Details of Products with image.
• 2. Hottest/Newest Items "Tapered in 100% Human Hair"
• 3. Store Page
Nice to have
• 1. My competitors is Morvine Eyelash. http://www.morvinelashes.com/
• Please follow the concepts of it.
• 2. www.Velkro.com: They have great products detail on the website.
• i would like to focus on "Tapered" for new styles of the eyelash.
• 3. I want to visitors can write down the "Reviews" in every single product.
• Please check the www.QELCosmetics.com.
Should not have
• It's not salon/Shop for the beauty.
• No need an appointment.
• We are the manufacturer of the eyelash.

```html
<!DOCTYPE html>
<html lang="en">
<head>
<meta charset="utf-8">
<title>Lunéva Eyelashes</title>
<link href="https://fonts.googleapis.com/css2?family=Open+Sans:wght@400;600&display=swap" rel="stylesheet">
<style>
:root{
  --gold:#b07a2a;
  --ink:#333;
  --muted:#777;
  --pink:#de2a5f;
  --sky:#5aa6d6;
  --red-a:#c0394a;--red-b:#9a1f2e;
  --mag-a:#c84aa8;--mag-b:#a52889;
  --amb-a:#d9a83a;--amb-b:#c2841e;
  --blu-a:#7ab4dc;--blu-b:#4b8fc2;
  --footer:#eeeeee;
  --base:#141414;
}
*{box-sizing:border-box;margin:0;padding:0}
html,body{width:1200px;height:1133px;overflow:hidden}
body{font-family:'Open Sans',sans-serif;color:var(--ink);background:#fff;position:relative}
a{color:inherit;text-decoration:none}
.abs{position:absolute}

/* header */
.brand{left:98px;top:22px;display:flex;flex-direction:column;line-height:1}
.brand-name{font-size:46px;font-weight:400;color:var(--gold);letter-spacing:-1px}
.brand-sub{font-size:15px;letter-spacing:5px;color:var(--ink);margin-top:6px}
.lang{top:50px;display:flex;gap:12px;left:698px}
.lang span{width:22px;height:15px;border:1px solid #ccc;font-size:8px;font-weight:600;display:flex;align-items:center;justify-content:center;color:#555;background:#f6f6f6}
.cart{left:776px;top:37px;display:flex;align-items:center}
.cart-btn{width:40px;height:40px;border-radius:50%;background:#d9334a;display:flex;align-items:center;justify-content:center;position:relative;z-index:1}
.cart-txt{border-top:1px solid #ddd;border-bottom:1px solid #ddd;padding:3px 12px 3px 10px;margin-left:-4px;line-height:1.2}
.cart-txt small{display:block;font-size:9px;color:#888}
.cart-txt b{font-weight:400;font-size:13px}
.search{left:903px;top:36px;width:196px;height:41px;border:1px solid #ccc;display:flex;align-items:center;justify-content:space-between;padding:0 12px 0 14px;font-size:12px;color:#888}

/* nav */
.rule{left:98px;top:129px;width:1002px;height:3px;background:#c9c9c9}
.nav{left:98px;top:134px;width:1002px;height:43px;display:flex;background:linear-gradient(#5a5a5a,#2e2e2e)}
.nav a{flex:auto;display:flex;align-items:center;justify-content:center;color:#ddd;font-size:12.5px;text-transform:uppercase;border-right:1px solid #222;box-shadow:inset -1px 0 0 #666}
.nav a:last-child{border:0;box-shadow:none}
.nav a.current{background:linear-gradient(#2b2b2b,#111);color:#fff;font-weight:600}

/* hero */
.hero{left:98px;top:183px;width:1002px;height:343px;background:linear-gradient(90deg,#f1cdbf 0%,#f8e6dc 45%,#f4d6c8 70%,#d9a99a 100%);overflow:hidden}
.hero-photo{position:absolute;right:0;top:0;width:330px;height:343px;background:radial-gradient(ellipse at 60% 45%,#d9a490 0%,#a8706a 45%,#4a2c34 100%)}
.hero-copy{position:absolute;left:134px;top:98px;width:470px}
.hero-copy h1{font-size:32px;font-weight:600;color:var(--pink);line-height:1.1}
.hero-copy p{font-size:14px;color:#555;margin-top:12px;line-height:1.5}
.hero-copy .btn{display:inline-block;margin-top:14px;border:1px solid #e6a6b1;border-radius:4px;background:#fff;padding:7px 13px;font-size:11px;color:#555}
.hero-prev{position:absolute;left:24px;top:157px}

/* products */
.section-title{left:99px;top:541px;font-size:22px;color:var(--sky);font-weight:400}
.pager{left:1065px;top:547px;display:flex;gap:2px}
.pager span{width:16px;height:16px;border:1px solid #bbb;display:flex;align-items:center;justify-content:center}
.card{top:584px;width:237px;height:217px;border:1px solid #ddd;border-bottom:0}
.card-img{height:150px;display:flex;align-items:center;justify-content:center;background:#fff}
.card-img div{width:98px;height:116px;border-radius:40px 40px 8px 8px}
.card-bar{position:absolute;left:-1px;right:-1px;bottom:0;height:66px;display:flex}
.card-info{flex:1;padding:14px 16px;color:#fff}
.card-info h3{font-size:16px;font-weight:600;line-height:1.1;text-transform:uppercase}
.card-info span{font-size:12.5px;font-weight:600}
.card-add{width:57px;display:flex;align-items:center;justify-content:center}
.c1 .card-info{background:var(--red-a)}.c1 .card-add{background:var(--red-b)}
.c2 .card-info{background:var(--mag-a)}.c2 .card-add{background:var(--mag-b)}
.c3 .card-info{background:var(--amb-a)}.c3 .card-add{background:var(--amb-b)}
.c4 .card-info{background:var(--blu-a)}.c4 .card-add{background:var(--blu-b)}

/* footer */
.footer{left:0;top:837px;width:1200px;height:206px;background:var(--footer)}
.fcol{top:874px}
.fcol h4{font-size:14px;font-weight:400;color:#333;margin-bottom:12px}
.fcol p{font-size:11.2px;color:#888;line-height:17px;width:205px}
.fcol .more{display:block;font-size:11px;color:#222;margin-top:8px}
.fcol ul{list-style:none}
.fcol li{font-size:11px;color:#888;line-height:22px}
.fcol li::before{content:"•";margin-right:7px;color:#aaa}
.vline{top:871px;width:1px;height:137px;background:#ccc}
.news h4{font-size:18px;font-weight:400;color:#444}
.news-field{display:flex;margin-top:8px;width:156px;height:27px}
.news-field span{flex:1;background:#fff;font-size:11px;color:#666;padding:6px 10px}
.news-field i{width:35px;background:linear-gradient(#e4e4e4,#bcbcbc);display:flex;align-items:center;justify-content:center}
.social{display:flex;gap:8px;margin-top:12px}
.social span{font-size:9px;color:#555;border:1px solid #aaa;padding:2px 4px}

.base{left:0;top:1043px;width:1200px;height:90px;background:var(--base)}
.copy{left:101px;top:1082px;font-size:11px;color:#888}
.pay{top:1078px;left:857px;display:flex;gap:8px;align-items:center}
.pay .card-mark{width:34px;height:22px;background:#f4f4f4;border-radius:2px;font-size:7.5px;font-weight:600;color:#333;display:flex;align-items:center;justify-content:center}
.pay .round{width:28px;height:28px;border:2px solid #fff;border-radius:50%;display:flex;align-items:center;justify-content:center}
.pay .round.dim{border-color:#888}
</style>
</head>
<body>

<header>
  <a class="abs brand" href="#"><span class="brand-name">LUNÉVA</span><span class="brand-sub">EYELASHES</span></a>
  <div class="abs lang"><span>EN</span><span>ES</span></div>
  <div class="abs cart">
    <div class="cart-btn"><svg width="16" height="14" viewBox="0 0 16 14"><path d="M0 1h3l2 8h8l2-6H4" fill="none" stroke="#fff" stroke-width="2"/><circle cx="6" cy="12" r="1.5" fill="#fff"/><circle cx="12" cy="12" r="1.5" fill="#fff"/></svg></div>
    <div class="cart-txt"><small>My Cart</small><b>0 items</b></div>
  </div>
  <div class="abs search">Search<svg width="14" height="14" viewBox="0 0 14 14"><circle cx="6" cy="6" r="4.5" fill="none" stroke="#333" stroke-width="2"/><path d="M9.5 9.5l3.5 3.5" stroke="#333" stroke-width="2"/></svg></div>
</header>

<div class="abs rule"></div>
<nav class="abs nav">
  <a class="current" href="#">Home</a><a href="#">About Us</a><a href="#">Products</a><a href="#">Contact Us</a><a href="#">Shipping</a><a href="#">My Account</a><a href="#">My Cart</a><a href="#">Checkout</a>
</nav>

<section class="abs hero">
  <div class="hero-photo" role="img" aria-label="Portrait of a model wearing tapered human hair lashes"></div>
  <svg class="hero-prev" width="14" height="26" viewBox="0 0 14 26"><path d="M12 1L2 13l10 12" fill="none" stroke="#999" stroke-width="2"/></svg>
  <div class="hero-copy">
    <h1>Tapered in 100% Human Hair</h1>
    <p>Pellentesque convallis molestie enim sit amet efficitur. Etiam id imperdiet lectus. Vivamus lacus justo, ultrices nec.</p>
    <a class="btn" href="#">Learn more</a>
  </div>
</section>

<h2 class="abs section-title">Our Products</h2>
<div class="abs pager">
  <span><svg width="8" height="8" viewBox="0 0 8 8"><path d="M5 1L2 4l3 3" fill="none" stroke="#333" stroke-width="1.5"/></svg></span>
  <span><svg width="8" height="8" viewBox="0 0 8 8"><path d="M3 1l3 3-3 3" fill="none" stroke="#333" stroke-width="1.5"/></svg></span>
</div>

<article class="abs card c1" style="left:99px">
  <div class="card-img"><div role="img" aria-label="Lash package, spring collection" style="background:linear-gradient(#f3b8c8,#e9e2e4)"></div></div>
  <div class="card-bar"><div class="card-info"><h3>Petaline</h3><span>$00.00</span></div><div class="card-add"><svg width="20" height="18" viewBox="0 0 16 14"><path d="M0 1h3l2 8h8l2-6H4" fill="none" stroke="#fff" stroke-width="2"/><circle cx="6" cy="12" r="1.5" fill="#fff"/><circle cx="12" cy="12" r="1.5" fill="#fff"/></svg></div></div>
</article>
<article class="abs card c2" style="left:354px">
  <div class="card-img"><div role="img" aria-label="Lash package, summer collection" style="background:linear-gradient(#f0b0c6,#e6dfe2)"></div></div>
  <div class="card-bar"><div class="card-info"><h3>Petaline</h3><span>$00.00</span></div><div class="card-add"><svg width="20" height="18" viewBox="0 0 16 14"><path d="M0 1h3l2 8h8l2-6H4" fill="none" stroke="#fff" stroke-width="2"/><circle cx="6" cy="12" r="1.5" fill="#fff"/><circle cx="12" cy="12" r="1.5" fill="#fff"/></svg></div></div>
</article>
<article class="abs card c3" style="left:608px">
  <div class="card-img"><div role="img" aria-label="Lash package, autumn collection" style="background:linear-gradient(#b0703a,#6b4a3a)"></div></div>
  <div class="card-bar"><div class="card-info"><h3>Petaline</h3><span>$00.00</span></div><div class="card-add"><svg width="20" height="18" viewBox="0 0 16 14"><path d="M0 1h3l2 8h8l2-6H4" fill="none" stroke="#fff" stroke-width="2"/><circle cx="6" cy="12" r="1.5" fill="#fff"/><circle cx="12" cy="12" r="1.5" fill="#fff"/></svg></div></div>
</article>
<article class="abs card c4" style="left:862px">
  <div class="card-img"><div role="img" aria-label="Lash package, winter collection" style="background:linear-gradient(#c9dbe8,#dcdfe6)"></div></div>
  <div class="card-bar"><div class="card-info"><h3>Petaline</h3><span>$00.00</span></div><div class="card-add"><svg width="20" height="18" viewBox="0 0 16 14"><path d="M0 1h3l2 8h8l2-6H4" fill="none" stroke="#fff" stroke-width="2"/><circle cx="6" cy="12" r="1.5" fill="#fff"/><circle cx="12" cy="12" r="1.5" fill="#fff"/></svg></div></div>
</article>

<footer>
  <div class="abs footer"></div>
  <div class="abs fcol" style="left:100px">
    <h4>About us</h4>
    <p>Praesent convallis placerat lorem, quis tincidunt lorem feugiat sed quam non sapien faucibus consequat vitae sit amet orci augue magna, placerat eget nulla non, congue suscipit neque</p>
    <a class="more" href="#">Read more</a>
  </div>
  <div class="abs vline" style="left:337px"></div>
  <div class="abs fcol" style="left:383px">
    <h4>Links</h4>
    <ul><li>Home</li><li>About us</li><li>Products</li><li>Contact us</li><li>Shipping</li></ul>
  </div>
  <div class="abs fcol" style="left:496px;top:904px">
    <ul><li>My Account</li><li>My Cart</li><li>Checkout</li></ul>
  </div>
  <div class="abs fcol" style="left:623px">
    <h4>Other Links</h4>
    <ul><li>Terms of Uss</li><li>Privacy Policy</li><li>Help</li><li>Sitemap</li></ul>
  </div>
  <div class="abs fcol" style="left:771px">
    <h4>Other Links</h4>
    <ul><li>Terms of Uss</li><li>Privacy Policy</li><li>Help</li><li>Sitemap</li></ul>
  </div>
  <div class="abs vline" style="left:892px"></div>
  <div class="abs fcol news" style="left:944px;top:868px">
    <h4>Newsletter</h4>
    <div class="news-field"><span>E-mail</span><i><svg width="12" height="14" viewBox="0 0 12 14"><path d="M1 1l10 6-10 6z" fill="#777"/></svg></i></div>
    <h4 style="margin-top:16px">Follow us on</h4>
    <div class="social"><span>Friendo</span><span>Streamo</span><span>Workly</span></div>
  </div>

  <div class="abs base"></div>
  <p class="abs copy">Copyright © 2015 Lunéva. All Rights Reserved.</p>
  <div class="abs pay">
    <span class="card-mark">PayNest</span><span class="card-mark">Quorra</span><span class="card-mark" style="background:#1c4a8c;color:#fff">Velta Pro</span><span class="card-mark">Velta</span>
    <span class="round"><svg width="12" height="9" viewBox="0 0 12 9"><rect x="0.5" y="0.5" width="11" height="8" fill="none" stroke="#fff"/><path d="M0.5 0.5l5.5 4 5.5-4" fill="none" stroke="#fff"/></svg></span>
    <span class="round dim"><svg width="12" height="12" viewBox="0 0 12 12"><path d="M6 11V1M1 6l5-5 5 5" fill="none" stroke="#888" stroke-width="1.5"/></svg></span>
  </div>
</footer>

</body>
</html>
```